Cafe / Bistro Website with a focus on Salads

I will be creating a wordpress site from the psds that you provide to me, i have attached a questionnaire and the answers to them to get an idea of what I'm looking for.

Reason: Id like to provide more time for designers to submit your designs, good luck!

Target Market(s)

20 - 45 years old downtown professionals

Industry/Entity Type

Cafe

Number of Pages Required

1 page

Requirements
Must have
• 1. Describe the products/services you sell.
• Cafe is open for breakfast and lunch serving fresh, made from scratch
• food and bakery items with an emphasis on their Fresh Bakery, Coffee,
• Panini & Deli Sandwiches, Fresh Salads with Homemade Dressings,
• Retail Items and Breakfast Items. (salads and dressings are their hottest
• selling items)
• 2. Age range of your target client base
• 20 - 45 years old
• Project-related questions
• 3. Technical skill level of your client base. Have a scale ranging from zero to ten with zero
• being the least technologically skilled and ten being the best.
• From 8 to 9 scale for tech savvy customers so mobile friendly is a must
• have.
Nice to have
• 4. Will your visitors require any special needs? Mobile version of site, multiple language
• support, larger type for easier reading, etc.)
• Just need the mobile friendly version as well.
• 5. Imagine your website in 5 years from now. Complete the sentence: I know my website works
• because…
• I know my website works because we have seen an increase in steady
• business and we are seeing new customers because of our online
• presence.
• 6. Name 3 things that are most important about the design of your new website.
• Branding matches our store look and feel, website has a clean look and
• its easy to read/user friendly.
• 7. Name 3 things that is least important in the design of your new website.
• 12. We don't need very much content, just enough to get them interested
• in visiting our store.
• 8. Do you have any color preferences, existing brand colors, and/or colors you do/not wish to
• include?
• Yes, we have uploaded a few interior pics not to be used on the site, but
• mainly for color and wood texture examples. Do your best to match the
• wood grain textures and the colors. A fun coffee cup similar to ours
• would be cool if its easy to create in Illustrator or Photoshop.
• 9. What are some existing websites that appeal to you? Provide links if possible.
• Not sure what sites I like that fit our store look and feel, sorry ;(
• © All Rights Reserved by lumen Brightpath IT 3
• Additional questions
• 10. Is your logo and other imagery web ready?
• 11. Do you have all images that you would like to be included in your website or would you like
• the designer to use imagery where appropriate?
• We can use stock photography where they see appropriate. I would like
• to use my food photos and merchandise photos, but maybe those are not
• seen on the home page? We can adjust once we see the first draft of the
• website designs.
• 12. Any specific features you would like included? Log in ability, calendars, forums, blog,
• subscription services (RSS, email or newsletters)?
• The only feature I could see using would be a calendar with days listing
• my type of soups and daily specials available. I should be able to know
• what those items are the last week of the month for the upcoming month.
• That would be cool and force me to be more organized with thinking
• ahead of time.
• PICKS RELATED AND MENTIONED ABOVE CAN ALL BE
• FOUND HERE…
• https://www.filevaultra.com/sh/qtrbwmkeyzlpaxv/BBkTpQ4mNcWuZyrfdhSJqoPa?dl=0

```html
<!DOCTYPE html>
<html lang="en">
<head>
<meta charset="utf-8">
<title>Juno's Cafe</title>
<link href="https://fonts.googleapis.com/css2?family=Almendra:wght@400;700&family=Roboto+Condensed:wght@300;400;700&display=swap" rel="stylesheet">
<style>
:root{
  --orange:#f7a21b;
  --orange-light:#f9b445;
  --gold:#f2a60d;
  --maroon:#6b1414;
  --ink:#555;
  --ink-soft:#888;
  --white:#fff;
  --panel:#ececec;
  --lilac:#f8f6fc;
  --wood:#7a3a1c;
  --field:rgba(255,255,255,.22);
  --field-line:rgba(255,255,255,.45);
  --pink:#d59aa8;
  --sand:#ddd19a;
  --aqua:#8fd3d8;
  --teal:#85cdbd;
  --rose:#e3989d;
  --leaf:#bcdca0;
}
*{box-sizing:border-box;margin:0;padding:0}
html,body{width:689px;height:1200px;overflow:hidden;background:var(--white)}
body{font-family:"Roboto Condensed",Arial,sans-serif;color:var(--ink)}
.page{position:relative;width:689px;height:1200px;overflow:hidden}
.abs{position:absolute}
.display{font-family:"Almendra",Georgia,serif;font-weight:700}

/* hero */
.hero{left:0;top:0;width:689px;height:282px;
  background:radial-gradient(ellipse at 45% 55%,#b85a52 0%,#7d3a2c 35%,#4a2116 70%,#2e140c 100%)}
.hero-shade{left:0;top:0;width:689px;height:282px;background:rgba(40,15,10,.35)}
.nav{left:129px;top:39px;width:431px;height:34px;background:var(--white);
  box-shadow:0 2px 4px rgba(0,0,0,.25)}
.nav-ribbon-l{left:120px;top:43px;width:14px;height:30px;background:#f1eee9;clip-path:polygon(0 0,100% 0,100% 100%,0 100%,45% 50%)}
.nav-search{left:538px;top:49px;width:22px;height:22px}
.nav-links{display:flex;gap:0;font-family:"Almendra",Georgia,serif;font-weight:700;font-size:9.5px;color:var(--maroon);top:51px}
.nav-links span{padding:0 5px;position:relative}
.nav-links span+span::before{content:"";position:absolute;left:-2px;top:5px;width:3px;height:3px;border-radius:50%;background:var(--orange)}
.nav-left{left:172px}
.nav-right{left:397px}
.brand{left:314px;top:18px;width:70px;height:70px;border-radius:50%;background:var(--white);
  display:flex;flex-direction:column;align-items:center;justify-content:center;box-shadow:0 1px 3px rgba(0,0,0,.2)}
.brand-name{font-family:"Almendra",Georgia,serif;font-weight:700;font-size:12px;color:var(--maroon);line-height:1;text-align:center}
.brand-phone{left:314px;top:96px;width:70px;text-align:center;font-size:5px;letter-spacing:1px;color:var(--maroon);font-weight:700}
.hero-kicker{left:0;top:145px;width:689px;text-align:center;color:var(--white);font-size:11px;font-weight:300}
.hero-title{left:0;top:160px;width:689px;text-align:center;color:var(--white);font-size:23px;letter-spacing:.3px}

/* feature strip */
.strip{left:129px;top:253px;width:431px;height:57px;display:flex}
.strip-item{width:70px;height:57px;background:var(--orange);color:var(--white);font-size:7px;text-align:center;
  display:flex;flex-direction:column;align-items:center;padding-top:8px;line-height:1.3;border-right:1px solid rgba(0,0,0,.05)}
.strip-item.active{background:var(--orange-light)}
.strip-item svg{margin-bottom:5px}
.special{width:151px;height:57px;background:var(--panel);position:relative}
.special-photo{left:6px;top:13px;width:58px;height:30px;border-radius:50%;
  background:radial-gradient(ellipse,#c96a33 0%,#a3431f 55%,#e2c592 80%,#ddd 100%)}
.special-name{left:72px;top:5px;font-size:12px;color:#333}
.special-text{left:72px;top:22px;width:78px;font-size:5.5px;color:var(--ink-soft);line-height:1.45}
.price{left:539px;top:246px;width:30px;height:30px}

/* services */
.services-title{left:0;top:340px;width:689px;text-align:center;font-size:16px;color:#666;letter-spacing:.5px}
.services-rule{left:267px;top:361px;width:155px;height:8px}
.service{width:150px;height:45px}
.service-badge{left:0;top:0;width:37px;height:37px}
.service-head{left:44px;top:-1px;font-family:"Almendra",Georgia,serif;font-weight:700;font-size:9px;color:#555;white-space:nowrap}
.service-text{left:44px;top:11px;width:90px;font-size:6px;color:var(--ink-soft);line-height:1.4}

/* booking */
.booking{left:0;top:504px;width:689px;height:238px;
  background:radial-gradient(ellipse at 30% 40%,#4a3a2a 0%,#2c2118 45%,#1b140f 100%)}
.booking-head{top:535px;font-size:16px;color:var(--gold)}
.field{height:17px;background:var(--field);border:1px solid var(--field-line);color:#eee;font-size:6px;padding:5px 7px}
.btn{left:129px;top:692px;width:60px;height:17px;background:#b7841c;color:#f4e6c5;font-size:6.5px;text-align:center;line-height:17px}
.calendar{left:356px;top:563px;width:204px;height:102px;background:rgba(255,255,255,.2);border:1px solid var(--field-line);color:#f3f3f3}
.cal-month{left:0;top:7px;width:204px;text-align:center;font-size:8px}
.cal-grid{left:8px;top:30px;width:188px;display:grid;grid-template-columns:repeat(7,1fr);font-size:6.3px;text-align:center;row-gap:2px}
.cal-grid .dow{margin-bottom:1px}
.cal-grid .today{color:var(--gold)}
.plate{left:325px;top:709px;width:61px;height:61px;border-radius:50%;background:var(--white);box-shadow:0 3px 6px rgba(0,0,0,.35)}
.plate-food{left:331px;top:715px;width:49px;height:49px;border-radius:50%;
  background:radial-gradient(circle at 45% 45%,#d8a048 0%,#c2512d 35%,#8a8a52 60%,#f2f2f2 75%)}

/* highlight */
.highlight-band{left:0;top:839px;width:689px;height:181px;background:var(--lilac)}
.highlight-photo{left:129px;top:807px;width:215px;height:179px;
  background:radial-gradient(ellipse at 50% 45%,#e08a4a 0%,#a83a2a 30%,#5b3320 55%,#2a1a12 80%,#140d08 100%)}
.highlight-copy{left:344px;top:807px;width:216px;height:179px;
  background:radial-gradient(ellipse at 50% 40%,#9a4a24 0%,#7a3a1c 45%,#4e2210 100%)}
.highlight-title{left:344px;top:822px;width:216px;text-align:center;color:var(--white);font-size:12px}
.highlight-rule{left:430px;top:838px;width:42px;height:4px}
.highlight-text{left:362px;top:850px;width:180px;text-align:center;color:#f2e6dc;font-size:6.5px;line-height:1.6}
.slide-btn{top:950px;width:20px;height:20px}

/* footer */
.footer{left:0;top:1020px;width:689px;height:160px;
  background:radial-gradient(ellipse at 55% 45%,#4a3b2e 0%,#2a2119 50%,#17110d 100%)}
.foot-head{top:1056px;font-size:11px;color:var(--white)}
.foot-head em{font-style:normal;color:var(--orange)}
.foot-text{font-size:7px;line-height:1.55;color:#e6e0da}
.hours{left:281px;top:1073px;font-size:7px;color:#e6e0da}
.hours li{list-style:none;display:flex;align-items:center;gap:5px;height:13px}
.hours b{font-weight:400;color:var(--orange)}
.avatar{left:416px;top:1081px;width:32px;height:32px;border-radius:50%;background:linear-gradient(#d9d9d9,#9a9a9a);border:2px solid var(--white)}
.quote{left:458px;top:1080px;width:105px}
.quote-name{left:458px;top:1126px;font-size:6px;color:var(--orange)}
.to-top{left:327px;top:1170px;width:22px;height:12px}
.copyright{left:0;top:1180px;width:689px;height:20px;background:var(--white);text-align:center;font-size:5.5px;line-height:20px;color:#333}
</style>
</head>
<body>
<div class="page">

  <!-- hero -->
  <div class="abs hero" role="img" aria-label="Photo of a fresh salad bowl with apples, nuts and cheese on a wooden table"></div>
  <div class="abs hero-shade"></div>
  <div class="abs nav-ribbon-l"></div>
  <div class="abs nav"></div>
  <nav class="abs nav-links nav-left"><span>Home</span><span>About</span><span>Products</span></nav>
  <nav class="abs nav-links nav-right"><span>Services</span><span>Menu</span><span>Contact Us</span></nav>
  <svg class="abs nav-search" viewBox="0 0 22 22"><circle cx="10" cy="10" r="4" fill="none" stroke="#222" stroke-width="1.6"/><line x1="13" y1="13" x2="16" y2="16" stroke="#222" stroke-width="1.8"/></svg>
  <div class="abs brand"><span class="brand-name">Juno's<br>Cafe</span></div>
  <div class="abs brand-phone">555.014.2290</div>
  <p class="abs hero-kicker">Lorem ipsum dolor sit amet, consetetur sadipscing elitr</p>
  <h1 class="abs hero-title display">Lorem Ipsum dolor sit amet</h1>

  <!-- feature strip -->
  <div class="abs strip">
    <div class="strip-item">
      <svg width="14" height="14" viewBox="0 0 14 14"><path d="M2 2l10 10M12 2L2 12" stroke="#fff" stroke-width="1.8" stroke-linecap="round"/></svg>
      Lorem ipsum<br>dolor</div>
    <div class="strip-item">
      <svg width="14" height="14" viewBox="0 0 14 14"><path d="M2 6h8v3a3 3 0 0 1-3 3H5a3 3 0 0 1-3-3z" fill="#fff"/><path d="M10 7h1.5a1.3 1.3 0 0 1 0 2.6H10" fill="none" stroke="#fff"/></svg>
      Lorem ipsum<br>dolor</div>
    <div class="strip-item active">
      <svg width="14" height="14" viewBox="0 0 14 14"><circle cx="7" cy="7" r="5.5" fill="none" stroke="#fff" stroke-width="1.4"/><circle cx="5.5" cy="6" r="1" fill="#fff"/><circle cx="8.5" cy="8.5" r="1" fill="#fff"/></svg>
      Lorem ipsum<br>dolor</div>
    <div class="strip-item">
      <svg width="14" height="14" viewBox="0 0 14 14"><path d="M3 10a5 5 0 1 1 8-4H6z" fill="#fff"/></svg>
      Lorem ipsum<br>dolor</div>
    <div class="special">
      <div class="abs special-photo" role="img" aria-label="Photo of a pizza"></div>
      <div class="abs special-name display">pizza</div>
      <p class="abs special-text">Lorem ipsum dolor sit amet, consetetur sadipscing elitr, sed diam nonumy eirmod</p>
    </div>
  </div>
  <svg class="abs price" viewBox="0 0 30 30"><polygon points="15,0 19,5 26,4 25,11 30,15 25,19 26,26 19,25 15,30 11,25 4,26 5,19 0,15 5,11 4,4 11,5" fill="var(--gold)"/><text x="15" y="18.5" text-anchor="middle" font-family="Almendra,serif" font-weight="700" font-size="9" fill="#222">$12</text></svg>

  <!-- services -->
  <h2 class="abs services-title display">Services We Provide</h2>
  <svg class="abs services-rule" viewBox="0 0 155 8"><line x1="0" y1="3" x2="65" y2="3" stroke="#ccc"/><line x1="90" y1="3" x2="155" y2="3" stroke="#ccc"/><path d="M69 6a8 4 0 0 1 17 0z" fill="#888"/></svg>

  <div class="abs service" style="left:129px;top:380px">
    <svg class="abs service-badge" viewBox="0 0 37 37"><rect x="5" y="5" width="27" height="27" rx="9" fill="var(--pink)"/><path d="M13 14h9v9a2 2 0 0 1-2 2h-5a2 2 0 0 1-2-2z" fill="#fff"/></svg>
    <h3 class="abs service-head">Lorem ipsum dolor</h3>
    <p class="abs service-text">Lorem ipsum dolor sit amet, consetetur sadipscing elitr, sed diam nonumy eirmod tempor</p>
  </div>
  <div class="abs service" style="left:282px;top:380px">
    <svg class="abs service-badge" viewBox="0 0 37 37"><rect x="5" y="5" width="27" height="27" rx="9" fill="var(--sand)"/><path d="M11 22a7.5 7.5 0 0 1 15 0z M10 23h17" fill="#fff" stroke="#fff"/></svg>
    <h3 class="abs service-head">Lorem ipsum dolor</h3>
    <p class="abs service-text">Lorem ipsum dolor sit amet, consetetur sadipscing elitr, sed diam nonumy eirmod tempor</p>
  </div>
  <div class="abs service" style="left:431px;top:380px">
    <svg class="abs service-badge" viewBox="0 0 37 37"><rect x="5" y="5" width="27" height="27" rx="9" fill="var(--aqua)"/><rect x="12" y="14" width="13" height="9" rx="3" fill="#fff"/></svg>
    <h3 class="abs service-head">Lorem ipsum dolor</h3>
    <p class="abs service-text">Lorem ipsum dolor sit amet, consetetur sadipscing elitr, sed diam nonumy eirmod tempor</p>
  </div>
  <div class="abs service" style="left:129px;top:433px">
    <svg class="abs service-badge" viewBox="0 0 37 37"><rect x="5" y="5" width="27" height="27" rx="9" fill="var(--teal)"/><path d="M13 13l3 7M24 13l-3 7" stroke="#fff" stroke-width="2" stroke-linecap="round"/></svg>
    <h3 class="abs service-head">Lorem ipsum dolor</h3>
    <p class="abs service-text">Lorem ipsum dolor sit amet, consetetur sadipscing elitr, sed diam nonumy eirmod tempor</p>
  </div>
  <div class="abs service" style="left:282px;top:433px">
    <svg class="abs service-badge" viewBox="0 0 37 37"><rect x="5" y="5" width="27" height="27" rx="9" fill="var(--rose)"/><path d="M13 16h10l-1 9h-8z" fill="#fff"/></svg>
    <h3 class="abs service-head">Lorem ipsum dolor</h3>
    <p class="abs service-text">Lorem ipsum dolor sit amet, consetetur sadipscing elitr, sed diam nonumy eirmod tempor</p>
  </div>
  <div class="abs service" style="left:431px;top:433px">
    <svg class="abs service-badge" viewBox="0 0 37 37"><rect x="5" y="5" width="27" height="27" rx="9" fill="var(--leaf)"/><path d="M12 17h9l-1 8h-7z M22 20h4v5h-4z" fill="#fff"/></svg>
    <h3 class="abs service-head">Lorem ipsum dolor</h3>
    <p class="abs service-text">Lorem ipsum dolor sit amet, consetetur sadipscing elitr, sed diam nonumy eirmod tempor</p>
  </div>

  <!-- booking -->
  <div class="abs booking" role="img" aria-label="Dark photo of a panini sandwich and a coffee mug on a wooden table"></div>
  <h2 class="abs booking-head display" style="left:129px">Booking form</h2>
  <h2 class="abs booking-head display" style="left:357px">Conform Date</h2>
  <div class="abs field" style="left:129px;top:563px;width:106px">First Name *</div>
  <div class="abs field" style="left:239px;top:563px;width:105px">Last Name *</div>
  <div class="abs field" style="left:129px;top:585px;width:106px">E-mail *</div>
  <div class="abs field" style="left:239px;top:585px;width:105px">Phone No *</div>
  <div class="abs field" style="left:129px;top:608px;width:106px">Guest Number *</div>
  <div class="abs field" style="left:239px;top:608px;width:105px">1:30
    <svg class="abs" style="right:6px;top:6px" width="7" height="5" viewBox="0 0 7 5"><path d="M1 1l2.5 2.5L6 1" fill="none" stroke="#eee"/></svg></div>
  <div class="abs field" style="left:129px;top:630px;width:215px;height:57px"></div>
  <div class="abs btn">Send Booking</div>

  <div class="abs calendar">
    <svg class="abs" style="left:12px;top:9px" width="6" height="8" viewBox="0 0 6 8"><path d="M5 1L2 4l3 3" fill="none" stroke="#fff" stroke-width="1.3"/></svg>
    <div class="abs cal-month">April 2015</div>
    <svg class="abs" style="right:12px;top:9px" width="6" height="8" viewBox="0 0 6 8"><path d="M1 1l3 3-3 3" fill="none" stroke="#fff" stroke-width="1.3"/></svg>
    <div class="abs cal-grid">
      <span class="dow">Mo</span><span class="dow">Tu</span><span class="dow">We</span><span class="dow">Th</span><span class="dow">Fr</span><span class="dow">Sa</span><span class="dow">Su</span>
      <span></span><span></span><span>1</span><span>2</span><span>3</span><span>4</span><span>5</span>
      <span>6</span><span>7</span><span>8</span><span>9</span><span>10</span><span>11</span><span>12</span>
      <span>13</span><span>14</span><span>15</span><span>16</span><span class="today">17</span><span>18</span><span>19</span>
      <span>20</span><span>21</span><span>22</span><span>23</span><span>24</span><span>25</span><span>26</span>
      <span>27</span><span>28</span><span>29</span><span>30</span><span>20</span><span></span><span></span>
    </div>
  </div>
  <div class="abs plate"></div>
  <div class="abs plate-food" role="img" aria-label="Photo of a plated dish with salad and bread"></div>

  <!-- highlight -->
  <div class="abs highlight-band"></div>
  <div class="abs highlight-photo" role="img" aria-label="Photo of a salad bowl with strawberries, nuts and greens"></div>
  <div class="abs highlight-copy" role="img" aria-label="Wood grain texture background"></div>
  <h2 class="abs highlight-title">Lorem ipsum dolor sit amet</h2>
  <svg class="abs highlight-rule" viewBox="0 0 42 4"><rect x="0" y="1" width="42" height="2" rx="1" fill="none" stroke="#fff" stroke-width=".6"/></svg>
  <p class="abs highlight-text">Lorem ipsum dolor sit amet, consetetur sadipscing elitr, sed diam nonumy eirmod tempor invidunt ut labore et dolore magna aliquyam erat, sed diam voluptua. Lorem ipsum dolor sit amet, consetetur sadipscing elitr, sed diam nonumy eirmod tempor invidunt ut labore et dolore magna aliquyam erat, sed diam voluptua.</p>
  <svg class="abs slide-btn" style="left:432px" viewBox="0 0 20 20"><circle cx="10" cy="10" r="9.5" fill="#fff"/><path d="M11.5 6l-4 4 4 4" fill="none" stroke="#333" stroke-width="1.5"/></svg>
  <svg class="abs slide-btn" style="left:454px" viewBox="0 0 20 20"><circle cx="10" cy="10" r="9.5" fill="#fff"/><path d="M8.5 6l4 4-4 4" fill="none" stroke="#333" stroke-width="1.5"/></svg>

  <!-- footer -->
  <div class="abs footer" role="img" aria-label="Dark photo of a sandwich on a wooden board"></div>
  <h3 class="abs foot-head" style="left:129px"><em>About</em> Juno's Cafe</h3>
  <p class="abs foot-text" style="left:129px;top:1074px;width:130px">Lorem ipsum dolor sit amet, consetetur sadipscing elitr, sed diam nonumy eirmod tempor invidunt ut labore et dolore magna Lorem ipsum dolor sit amet, consetetur sadipscing elitr, sed diam nonumy eirmod tempor invidunt ut labore et dolore magna</p>
  <h3 class="abs foot-head" style="left:281px"><em>Bakery</em> Time</h3>
  <ul class="abs hours">
    <li><svg width="9" height="9" viewBox="0 0 9 9"><circle cx="4.5" cy="4.5" r="3.8" fill="none" stroke="#eee"/><path d="M4.5 2.5v2h1.5" fill="none" stroke="#eee"/></svg>Monday to Thuesday <b>7:00 - 19:00</b></li>
    <li><svg width="9" height="9" viewBox="0 0 9 9"><circle cx="4.5" cy="4.5" r="3.8" fill="none" stroke="#eee"/><path d="M4.5 2.5v2h1.5" fill="none" stroke="#eee"/></svg>Friday to Saturdays <b>12:00 - 22:00</b></li>
    <li><svg width="9" height="9" viewBox="0 0 9 9"><circle cx="4.5" cy="4.5" r="3.8" fill="none" stroke="#eee"/><path d="M4.5 2.5v2h1.5" fill="none" stroke="#eee"/></svg>Sundays Open</li>
  </ul>
  <h3 class="abs foot-head" style="left:416px"><em>Other</em> Said</h3>
  <div class="abs avatar" role="img" aria-label="Customer portrait photo"></div>
  <p class="abs foot-text quote">“Lorem ipsum dolor sit amet, consetetur sadipscing elitr, sed diam nonumy eirmod tempor invidunt ut labore et dolore magna”</p>
  <div class="abs quote-name">Orin Vale</div>
  <svg class="abs to-top" viewBox="0 0 22 12"><path d="M0 12a11 11 0 0 1 22 0z" fill="#fff"/><path d="M7 9l4-4 4 4" fill="none" stroke="#333" stroke-width="1.3"/></svg>
  <footer class="abs copyright">© All Rights Reserveu oy lumen Brightpath IT 3</footer>

</div>
</body>
</html>
```